Thermostat Screen Design

We need a screen layout design for a new thermostat we're currently developing. If you're not familiar with thermostats, you can see some examples here - http://smart-climate-units-guide.bestpickdigest.com/

We're after the main page design, with icons, colours etc. It needs to be clean, modern and minimalistic. Attached is all components required on the screen. The screen size is 5 inch (diagnol).

The arrows on the screen showcase what happens when you press a button. For example, when you press MODE once you get OFF, press it twice, HEAT, press it 3 times, COOL, etc. This is just for your reference.

You have complete creative license on how you choose to layout the screen, position the components etc, but we require:

- it must be on a 5 inch screen diagnol
- modern, clean and minimalistic
- includes icons and colours
- Intuitive

Let me know if any questions.

```html
<!DOCTYPE html>
<html lang="en">
<head>
<meta charset="utf-8">
<title>Thermostat Main Screen</title>
<link href="https://fonts.googleapis.com/css2?family=Barlow:wght@300;400;500&family=Barlow+Semi+Condensed:wght@300&display=swap" rel="stylesheet">
<style>
  :root {
    --sky-dusk: #4c4762;
    --sky-mauve: #8d7580;
    --glow-peach: #fbcf9e;
    --glow-orange: #f3964f;
    --ember: #dc5a3b;
    --ink-white: #ffffff;
    --ink-soft: rgba(255,255,255,0.55);
    --glass: rgba(255,255,255,0.16);
    --glass-strong: rgba(255,255,255,0.26);
    --bar-shade: rgba(40,34,60,0.32);
    --icon-tint: rgba(232,128,90,0.75);
  }
  * { box-sizing: border-box; margin: 0; padding: 0; }
  html, body { width: 1200px; height: 680px; overflow: hidden; }
  body { font-family: "Barlow", sans-serif; color: var(--ink-white); }

  .screen {
    position: relative; width: 1200px; height: 680px; overflow: hidden;
    background:
      radial-gradient(ellipse 520px 380px at 560px 260px, var(--glow-peach) 0%, rgba(251,207,158,0) 100%),
      radial-gradient(ellipse 900px 520px at 0 0, var(--sky-dusk) 0%, rgba(76,71,98,0) 70%),
      radial-gradient(ellipse 600px 400px at 1200px 60px, var(--sky-mauve) 0%, rgba(141,117,128,0) 80%),
      linear-gradient(180deg, #c9927e 0%, var(--glow-orange) 55%, var(--ember) 100%);
  }

  .status-bar {
    position: absolute; left: 0; top: 0; width: 100%; height: 85px;
    background: var(--bar-shade);
    display: flex; align-items: center;
  }
  .clock { font-size: 37px; font-weight: 400; padding-left: 26px; width: 139px; }
  .date-block { border-left: 1px solid rgba(255,255,255,0.3); height: 56px; padding-left: 18px; display: flex; flex-direction: column; justify-content: center; }
  .weekday { font-size: 25px; font-weight: 400; line-height: 1.15; }
  .day-month { font-size: 18px; color: var(--ink-soft); line-height: 1.2; }
  .night-toggle {
    position: absolute; right: 20px; top: 18px; width: 48px; height: 48px; border-radius: 50%;
    background: rgba(255,255,255,0.1); display: flex; align-items: center; justify-content: center;
  }

  .side-menu { position: absolute; left: 24px; top: 111px; }
  .menu-button {
    width: 96px; height: 96px; border-radius: 50%; background: var(--glass);
    display: flex; align-items: center; justify-content: center; margin-bottom: 24px;
  }

  .current-temp {
    position: absolute; left: 330px; top: 137px; width: 390px;
    font-family: "Barlow Semi Condensed", sans-serif;
    font-size: 360px; font-weight: 300; line-height: 1; letter-spacing: -8px;
    white-space: nowrap;
  }

  .setpoint {
    position: absolute; left: 736px; top: 170px; width: 110px; height: 332px; border-radius: 55px;
    background: var(--glass);
  }
  .setpoint-button {
    position: absolute; left: 17px; width: 76px; height: 76px; border-radius: 50%;
    background: var(--glass-strong); display: flex; align-items: center; justify-content: center;
  }
  .setpoint-up { top: 19px; }
  .setpoint-down { bottom: 19px; }
  .setpoint-value { position: absolute; left: 0; width: 100%; top: 142px; text-align: center; font-size: 38px; font-weight: 400; }

  .control-pill {
    position: absolute; top: 613px; height: 50px; border-radius: 25px; background: var(--glass);
    display: flex; align-items: center; justify-content: space-around; padding: 0 14px;
    font-size: 20px; font-weight: 400; color: var(--ink-soft);
  }
  .control-pill .active { color: var(--ink-white); font-weight: 500; }
  .mode-pill { left: 32px; width: 306px; }
  .fan-pill { left: 370px; width: 135px; justify-content: center; gap: 22px; }
  .system-pill { left: 530px; width: 215px; justify-content: center; gap: 22px; }
  .zone-pill { left: 769px; width: 406px; }
</style>
</head>
<body>
<main class="screen">
  <header class="status-bar">
    <div class="clock">09:32</div>
    <div class="date-block">
      <span class="weekday">Wednesday</span>
      <span class="day-month">August, 28</span>
    </div>
    <div class="night-toggle" aria-label="Night mode">
      <svg width="26" height="26" viewBox="0 0 26 26"><path d="M17 3a10 10 0 1 0 6 17A9 9 0 0 1 17 3z" fill="rgba(255,255,255,0.55)"/></svg>
    </div>
  </header>

  <nav class="side-menu">
    <div class="menu-button" aria-label="Dashboard">
      <svg width="52" height="52" viewBox="0 0 52 52" fill="var(--icon-tint)">
        <circle cx="14" cy="14" r="10" fill="none" stroke="var(--icon-tint)" stroke-width="4"/>
        <circle cx="38" cy="14" r="12"/><circle cx="14" cy="38" r="12"/><circle cx="38" cy="38" r="12"/>
      </svg>
    </div>
    <div class="menu-button" aria-label="Fan">
      <svg width="54" height="54" viewBox="0 0 54 54" fill="var(--icon-tint)">
        <path d="M27 27C20 24 12 10 22 6c8-3 10 10 5 21z"/>
        <path d="M27 27C30 20 44 12 48 22c3 8-10 10-21 5z"/>
        <path d="M27 27C34 30 42 44 32 48c-8 3-10-10-5-21z"/>
        <path d="M27 27C24 34 10 42 6 32c-3-8 10-10 21-5z"/>
        <circle cx="27" cy="27" r="4" fill="rgba(255,255,255,0.6)"/>
      </svg>
    </div>
    <div class="menu-button" aria-label="Settings">
      <svg width="54" height="54" viewBox="0 0 54 54">
        <g fill="var(--icon-tint)">
          <circle cx="27" cy="27" r="17"/>
          <rect x="21" y="3" width="12" height="12" rx="3"/><rect x="21" y="39" width="12" height="12" rx="3"/>
          <rect x="3" y="21" width="12" height="12" rx="3"/><rect x="39" y="21" width="12" height="12" rx="3"/>
          <g transform="rotate(45 27 27)">
            <rect x="21" y="3" width="12" height="12" rx="3"/><rect x="21" y="39" width="12" height="12" rx="3"/>
            <rect x="3" y="21" width="12" height="12" rx="3"/><rect x="39" y="21" width="12" height="12" rx="3"/>
          </g>
        </g>
        <circle cx="27" cy="27" r="7" fill="rgba(255,255,255,0.55)"/>
      </svg>
    </div>
    <div class="menu-button" aria-label="Zones">
      <svg width="60" height="60" viewBox="0 0 60 60" fill="none" stroke="var(--icon-tint)" stroke-width="5">
        <circle cx="30" cy="30" r="25"/><circle cx="30" cy="30" r="15"/><circle cx="30" cy="30" r="5" fill="var(--icon-tint)"/>
      </svg>
    </div>
  </nav>

  <div class="current-temp">15°</div>

  <section class="setpoint" aria-label="Target temperature">
    <div class="setpoint-button setpoint-up">
      <svg width="34" height="20" viewBox="0 0 34 20"><path d="M3 17L17 4l14 13" fill="none" stroke="var(--icon-tint)" stroke-width="4" stroke-linecap="round" stroke-linejoin="round"/></svg>
    </div>
    <div class="setpoint-value">25°</div>
    <div class="setpoint-button setpoint-down">
      <svg width="34" height="20" viewBox="0 0 34 20"><path d="M3 3l14 13L31 3" fill="none" stroke="var(--icon-tint)" stroke-width="4" stroke-linecap="round" stroke-linejoin="round"/></svg>
    </div>
  </section>

  <div class="control-pill mode-pill">
    <span>OFF</span><span class="active">HEAT</span><span>COOL</span><span>AUTO</span>
  </div>
  <div class="control-pill fan-pill">
    <svg width="26" height="26" viewBox="0 0 54 54" fill="rgba(255,255,255,0.55)">
      <path d="M27 27C20 24 12 10 22 6c8-3 10 10 5 21z"/><path d="M27 27C30 20 44 12 48 22c3 8-10 10-21 5z"/>
      <path d="M27 27C34 30 42 44 32 48c-8 3-10-10-5-21z"/><path d="M27 27C24 34 10 42 6 32c-3-8 10-10 21-5z"/>
    </svg>
    <span>AUTO</span>
  </div>
  <div class="control-pill system-pill">
    <svg width="26" height="26" viewBox="0 0 52 52" fill="rgba(255,255,255,0.55)">
      <circle cx="14" cy="14" r="10" fill="none" stroke="rgba(255,255,255,0.55)" stroke-width="5"/>
      <circle cx="38" cy="14" r="12"/><circle cx="14" cy="38" r="12"/><circle cx="38" cy="38" r="12"/>
    </svg>
    <span class="active">HEAT</span><span>COOL</span>
  </div>
  <div class="control-pill zone-pill">
    <svg width="28" height="28" viewBox="0 0 60 60" fill="none" stroke="rgba(255,255,255,0.55)" stroke-width="6">
      <circle cx="30" cy="30" r="25"/><circle cx="30" cy="30" r="13"/><circle cx="30" cy="30" r="3" fill="rgba(255,255,255,0.55)"/>
    </svg>
    <span>ZONE 1</span><span>ZONE 2</span><span class="active">ZONE 3</span><span>ZONE 4</span>
  </div>
</main>
</body>
</html>
```